Tiroler party ecommerce site

We have a eCommerce site that needs a redesign. What we need are 3 pages: a frontpage, a product listing page and a product page.

The look has to be:
fun, modern, fresh, bright, professional look but not corporate.

Some content keywords are :
Carnival, oktoberfesten, tirol, dirndl, leder hosen, beer, women with big breast (no porn! just fun)

Some functional hints :

The frontpage needs to give a good impression of all the products on the site.
There should also be some space for campaigns or banners on the frontpage.

The product listing page should have facets (search options) and a search field.

The product page should have a few boxes such as related products, others viewed, comments etc.. (your average product page content)

All pages should show a small cart button or box and off course a kick ass menu!

Some links :

The current site http://www.bergfeestwinkel.nl/

We couldn't find any site to show as inspiration most party sites are very bad!.

```html
<!DOCTYPE html>
<html lang="en">
<head>
<meta charset="utf-8">
<title>Bergfeestwinkel – Product</title>
<link href="https://fonts.googleapis.com/css2?family=Arimo:wght@400;700&display=swap" rel="stylesheet">
<style>
:root{
  --green:#65ac0b;
  --green-dark:#4e8a05;
  --dark:#2b2b2b;
  --text:#555;
  --muted:#999;
  --line:#e2e2e2;
  --panel:#f0f0f0;
  --white:#fff;
  --red:#e0201b;
  --star-off:#bdbdbd;
}
*{box-sizing:border-box;margin:0;padding:0}
html,body{width:1200px;height:1089px;overflow:hidden;font-family:"Arimo",Arial,sans-serif;color:var(--text);background:var(--white)}
.canvas{position:relative;width:1200px;height:1089px;overflow:hidden}
.abs{position:absolute}
a{color:inherit;text-decoration:none}

.topbar{left:0;top:0;width:1200px;height:22px;background:#f3f3f3;font-size:7.5px;color:#888}
.topbar .welcome{position:absolute;left:240px;top:7px}
.topbar .welcome b{color:#333}
.topbar .welcome .create{color:var(--green);font-weight:700}
.currency{position:absolute;top:0;height:22px;width:48px;background:#e6e6e6;color:#aaa;text-align:center;line-height:22px}
.toplinks{position:absolute;left:826px;top:7px;color:#333}
.toplinks span{margin:0 6px;color:#888}

.backdrop{left:0;top:160px;width:1200px;height:853px;
  background:linear-gradient(90deg,#55605a 0%,#7c8a7a 6%,#9aa695 12%,#b7c0a8 17%,#a9b2a0 20%,#c8d0b8 80%,#9fb4c2 86%,#6f93b0 90%,#b8c6a2 96%,#d6dcae 100%)}
.band{left:0;top:1013px;width:1200px;height:76px;background:var(--green)}

.page{left:240px;top:112px;width:742px;height:957px;background:var(--panel)}
.header-white{left:0;top:22px;width:1200px;height:138px;background:var(--white)}

.logo{left:240px;top:62px;width:160px;height:44px}
.logo .name{position:absolute;left:0;top:10px;font-size:26px;font-weight:400;color:var(--green);letter-spacing:-.5px}
.logo .tag{position:absolute;left:118px;top:0;font-size:8.5px;color:#444;line-height:10px;text-align:right}

.search{left:424px;top:71px;width:386px;height:26px;border:1px solid #ccc;background:var(--white);font-size:7.5px;color:#888}
.search .cat{position:absolute;left:0;top:0;width:104px;height:24px;border-right:1px solid #ddd;padding:8px 0 0 20px}
.search .cat svg{position:absolute;right:6px;top:10px}
.search .field{position:absolute;left:118px;top:8px}
.search .go{position:absolute;right:0;top:0;width:25px;height:24px;background:var(--green)}
.search .go svg{position:absolute;left:6px;top:5px}

.minicart{left:832px;top:71px;width:149px;height:26px;border:1px solid #ccc;background:#f7f7f7;font-size:8.5px;color:#444}
.minicart svg.cart{position:absolute;left:14px;top:7px}
.minicart .sum{position:absolute;left:41px;top:8px}
.minicart .drop{position:absolute;right:0;top:0;width:26px;height:24px;border-left:1px solid #ccc}
.minicart .drop svg{position:absolute;left:8px;top:10px}

.nav{left:258px;top:131px;width:704px;height:29px;background:var(--green);font-size:8px;color:var(--white)}
.nav .plist{position:absolute;left:0;top:0;width:147px;height:29px;background:var(--dark);font-weight:700;padding:11px 0 0 15px}
.nav .plist svg{position:absolute;right:14px;top:12px}
.nav .item{position:absolute;top:11px}
.nav .basket{position:absolute;right:0;top:0;width:101px;height:29px;background:var(--dark);font-weight:700;padding:10px 0 0 34px}
.nav .basket svg{position:absolute;left:15px;top:9px}

.sidebox{background:var(--white);border:1px solid #ddd}
.cats{left:258px;top:160px;width:147px;height:216px;padding:8px 15px 0 14px;font-size:7.5px;color:#555}
.cats li{list-style:none;height:21.3px;padding-top:6px;border-bottom:1px dashed #ccc}
.cats li:last-child{border-bottom:0}
.cats li.active{color:var(--green);border-bottom:1px dashed var(--green)}
.news{left:258px;top:381px;width:147px;height:216px;text-align:center}
.news h3{font-size:9.5px;font-weight:400;color:#555;margin-top:22px}
.news .thumb{width:44px;height:88px;margin:10px auto 0;background:linear-gradient(180deg,#e9d2bb 0%,#f3f0ea 35%,#3f7d3a 55%,#e9d2bb 80%,#f4f4f4 100%);border-radius:4px}
.news p{font-size:7px;line-height:12px;color:#555;margin:10px 8px 0}
.news .stars{margin-top:7px;font-size:10px}
.news .all{display:block;font-size:6px;color:#333;text-decoration:underline;margin-top:6px}

.star{color:var(--green)}
.star.off{color:var(--star-off)}

.main{left:409px;top:160px;width:553px;height:649px;background:var(--white)}
.photo{left:468px;top:186px;width:110px;height:222px;background:linear-gradient(180deg,#f2f2f2 0%,#e8d4c3 15%,#ffffff 28%,#b47a3b 45%,#c98d4a 55%,#f2e6da 70%,#ffffff 85%,#8a4a2a 97%,#f5f5f5 100%);border-radius:8px}

.info{left:662px;top:190px;width:272px}
.info h1{font-size:14px;font-weight:400;color:#333;padding-bottom:10px;border-bottom:1px solid var(--line)}
.price{margin-top:16px;font-size:10px;font-weight:700;color:#444}
.price .old{color:#aaa;text-decoration:line-through;font-weight:400;margin-left:2px}
.price .new{color:var(--green);margin-left:12px}
.meta{margin-top:8px;font-size:7.5px;line-height:10.7px;color:#aaa}
.meta b{color:#333;font-weight:400}
.info .stars{font-size:10px;margin-top:4px}
.opt-label{font-size:8px;color:#333;margin-top:10px}
.select{margin-top:6px;width:129px;height:23px;border:1px solid #ccc;font-size:7px;color:#aaa;padding:7px 0 0 9px;position:relative}
.select svg{position:absolute;right:8px;top:9px}
.buy{margin-top:9px;height:23px;position:relative;font-size:8px;color:#333}
.buy .qty{position:absolute;left:19px;top:0;width:34px;height:22px;border:1px solid #ccc;padding:6px 0 0 10px;color:#888}
.buy .label{position:absolute;left:0;top:7px}
.buy .add{position:absolute;left:56px;top:0;width:74px;height:22px;background:var(--green);color:var(--white);text-align:center;line-height:22px}
.extras{margin-top:9px;font-size:6.5px;color:#aaa}
.extras span{margin-right:12px}

.tabs{left:438px;top:432px;width:496px;height:28px;border-top:1px solid #ccc;border-bottom:1px solid #ddd;font-size:8px;color:#555}
.tabs .tab{position:absolute;top:9px}
.tabs .active{left:25px;top:-1px;width:77px;height:28px;background:var(--green);color:var(--white);text-align:center;line-height:27px}
.tabs .active svg{position:absolute;left:35px;top:27px}

.desc{left:462px;top:475px;width:228px}
.desc h2{font-size:8px;font-weight:700;color:#777}
.desc p{margin-top:9px;font-size:7px;line-height:11px;color:#999}

.spec{left:718px;top:473px;width:204px;font-size:7.5px;color:#777;border-collapse:collapse}
.spec th{background:var(--green);color:var(--white);text-align:left;font-weight:400;height:17px;padding-left:12px}
.spec td{height:17.5px;padding-left:12px;width:50%}
.spec tr:nth-child(odd) td{background:#f2f2f2}

.rel-rule{left:432px;top:607px;width:502px;height:1px;background:#eee}
.rel-title{left:432px;top:620px;font-size:10px;color:#555}
.rel-rule2{left:432px;top:641px;width:502px;height:1px;background:#eee}
.card{width:85px;top:656px;font-size:7.5px}
.card .img{width:85px;height:89px;border:1px solid #ddd}
.card.active .img{border-color:var(--green)}
.card .n{margin-top:12px;color:#555}
.card.active .n{color:var(--green)}
.card .p{margin-top:4px;font-size:7px}
.card .p s{color:#999}
.card .p em{font-style:normal;color:var(--red);margin-left:4px}
.card .stars{font-size:9px;margin-top:2px}
.blonde{background:linear-gradient(180deg,#fff 0%,#f1dca0 25%,#f2d3bd 45%,#fff 60%,#2c2c2c 80%,#c62020 90%,#fff 100%)}
.greendress{background:linear-gradient(180deg,#fff 0%,#e4c9a9 25%,#fff 45%,#a03a3a 60%,#3d7d3a 80%,#fff 100%)}
.browndress{background:linear-gradient(180deg,#fff 0%,#5a3424 20%,#f3ddc9 40%,#3a2a20 60%,#c98d4a 80%,#fff 100%)}

.partners{left:258px;top:823px;width:704px;height:55px;background:var(--white)}
.partner{position:absolute;top:17px;font-size:11px;font-weight:700;color:#555;display:flex;align-items:center;gap:5px}
.partner i{display:inline-block;width:12px;height:12px;background:var(--green);border-radius:50%}
.partners .sep{position:absolute;top:14px;width:1px;height:28px;background:#ddd}

.foot h4{font-size:9px;font-weight:400;color:#333}
.foot .rule{height:1px;background:#ddd;margin-top:10px}
.foot ul{list-style:none;font-size:7px;color:#555;line-height:10.7px}
.site{left:258px;top:900px;width:225px}
.blog{left:534px;top:900px;width:120px}
.blog li{border-bottom:1px solid #ddd;padding:7px 0 3px}
.letter{left:703px;top:900px;width:112px}
.letter .mail{margin-top:18px;display:flex;height:23px;font-size:7px}
.letter .mail span{flex:1;border:1px solid #ccc;padding:7px 0 0 5px;color:#999}
.letter .mail b{width:21px;background:var(--green);color:#222;text-align:center;line-height:23px;font-weight:400}
.social{left:866px;top:900px;width:96px}
.social .dots{margin-top:18px;display:flex;gap:7px}
.social .dots i{width:16px;height:16px;border-radius:50%;background:#aaa;display:block}

.copyline{left:258px;top:1018px;width:704px;height:1px;background:#ddd}
.copy{left:258px;top:1031px;font-size:7px;color:#555}
.cards{left:856px;top:1028px;display:flex;gap:3px}
.cards span{width:35px;height:22px;border:1px solid #ccc;background:var(--white);font-size:7.5px;font-weight:700;color:#334;text-align:center;line-height:20px}
</style>
</head>
<body>
<div class="canvas">

  <div class="abs backdrop" role="img" aria-label="Soft blurred photo backdrop in green, grey and blue tones"></div>
  <div class="abs band"></div>
  <div class="abs header-white"></div>
  <div class="abs page"></div>

  <div class="abs topbar">
    <div class="welcome">WELCOME VISITOR YOU CAN <b>LOGIN</b> OR <span class="create">CREATE AN ACCOUNT</span></div>
    <div class="currency" style="left:710px">EUR €</div>
    <div class="currency" style="left:760px">GBP £</div>
    <div class="toplinks">My Account<span>|</span>Shopping Cart<span>|</span>Checkout</div>
  </div>

  <div class="abs logo">
    <div class="tag">online<br>shopping</div>
    <div class="name">Bergfeestwinkel</div>
  </div>

  <div class="abs search">
    <div class="cat">All Categories<svg width="7" height="4"><path d="M0 0h7L3.5 4z" fill="#999"/></svg></div>
    <div class="field">Search Entire Store here</div>
    <div class="go"><svg width="13" height="13" viewBox="0 0 13 13"><circle cx="5.5" cy="5.5" r="4" fill="none" stroke="#fff" stroke-width="1.6"/><path d="M8.5 8.5l3.5 3.5" stroke="#fff" stroke-width="1.8"/></svg></div>
  </div>

  <div class="abs minicart">
    <svg class="cart" width="16" height="12" viewBox="0 0 16 12"><path d="M0 1h3l2 7h8l2-5H4" fill="none" stroke="#555" stroke-width="1.3"/><circle cx="6" cy="10.5" r="1.2" fill="#555"/><circle cx="12" cy="10.5" r="1.2" fill="#555"/></svg>
    <div class="sum">0 ITEM(S) - $0.00</div>
    <div class="drop"><svg width="9" height="5"><path d="M0 0h9L4.5 5z" fill="#555"/></svg></div>
  </div>

  <div class="abs nav">
    <div class="plist">PRODUCTS LIST<svg width="8" height="5"><path d="M0 0l4 4 4-4" fill="none" stroke="#fff" stroke-width="1.4"/></svg></div>
    <span class="item" style="left:190px">HOME</span>
    <span class="item" style="left:264px">INFORMATIE</span>
    <span class="item" style="left:365px">LINKS</span>
    <span class="item" style="left:438px">CONTACT</span>
    <div class="basket"><svg width="14" height="11" viewBox="0 0 16 12"><path d="M0 1h3l2 7h8l2-5H4" fill="none" stroke="#fff" stroke-width="1.4"/><circle cx="6" cy="10.5" r="1.2" fill="#fff"/><circle cx="12" cy="10.5" r="1.2" fill="#fff"/></svg>Winkelwagen</div>
  </div>

  <ul class="abs sidebox cats">
    <li>Lorem Ipsum</li><li>Lorem</li><li>Lorem Ipsum</li><li>Lorem Ipsum Lorem</li>
    <li>Lorem Ipsum</li><li>Lorem</li><li class="active">Lorem Ipsum</li><li>Lorem Ipsum</li>
  </ul>

  <div class="abs sidebox news">
    <h3>What's New?</h3>
    <div class="thumb" role="img" aria-label="Product photo: woman in green dirndl holding a beer stein"></div>
    <p>Lorem Ipsum is simply dummy text of the printing and typesetting</p>
    <div class="stars"><span class="star">★★★</span><span class="star off">★★</span></div>
    <a class="all">VIEW ALL</a>
  </div>

  <div class="abs main"></div>
  <div class="abs photo" role="img" aria-label="Product photo: woman in brown dirndl costume with white knee socks"></div>

  <div class="abs info">
    <h1>Product Name - Lorem Ipsum</h1>
    <div class="price">Price: <span class="old">$150.00</span><span class="new">$120.00</span></div>
    <div class="meta">Ex Tax: <b>$300</b><br>Brand: <b>Lorem Ipsum</b><br>Product Code: <b>SKU 1732</b><br>Availability: <b>In Stock</b></div>
    <div class="stars"><span class="star">★★★</span><span class="star off">★★</span></div>
    <div class="opt-label">Other Option</div>
    <div class="select">Please Select<svg width="7" height="4"><path d="M0 0h7L3.5 4z" fill="#999"/></svg></div>
    <div class="buy"><span class="label">Qty</span><span class="qty">2</span><span class="add">Add to Cart</span></div>
    <div class="extras"><span>♥ Add to Wishlist</span><span>⇄ Add to Compare</span></div>
  </div>

  <div class="abs tabs">
    <div class="tab active">Description<svg width="8" height="4"><path d="M0 0h8L4 4z" fill="#65ac0b"/></svg></div>
    <span class="tab" style="left:146px">Accessories</span>
    <span class="tab" style="left:229px">Downloads</span>
    <span class="tab" style="left:311px">Reviews (0)</span>
  </div>

  <div class="abs desc">
    <h2>Lorem Ipsum is simply dummy text</h2>
    <p>The printing and typesetting industry. Lorem Ipsum has been the industry's standard dummy text ever since the 1500s, when an unknown printer took a galley of type and scrambled it to make a type specimen book. It has survived not only five centuries, but also the leap into electronic typesetting, remaining essentially</p>
  </div>

  <table class="abs spec">
    <tr><th colspan="2">Specification</th></tr>
    <tr><td>Brand</td><td>Lorem Ipsum</td></tr>
    <tr><td>Model</td><td>Lorem Ipsum dummy</td></tr>
    <tr><td>Manufacturer Warranty</td><td>Lorem Ipsum dummy</td></tr>
    <tr><td>Other Option</td><td>Lorem Ipsum</td></tr>
  </table>

  <div class="abs rel-rule"></div>
  <div class="abs rel-title">Related Products</div>
  <div class="abs rel-rule2"></div>

  <div class="abs card" style="left:432px"><div class="img blonde" role="img" aria-label="Product photo: blonde braided wig"></div><div class="n">Lorem Ipsum Name</div><div class="p"><s>$ 12.00</s><em>$ 09.00</em></div><div class="stars"><span class="star">★★★</span><span class="star off">★★</span></div></div>
  <div class="abs card" style="left:534px"><div class="img greendress" role="img" aria-label="Product photo: green dirndl with beer stein"></div><div class="n">Lorem Ipsum Name</div><div class="p"><s>$ 12.00</s><em>$ 09.00</em></div><div class="stars"><span class="star">★★★</span><span class="star off">★★</span></div></div>
  <div class="abs card active" style="left:640px"><div class="img browndress" role="img" aria-label="Product photo: brown dirndl costume"></div><div class="n">Lorem Ipsum Name</div><div class="p"><s>$ 12.00</s><em>$ 09.00</em></div><div class="stars"><span class="star">★★★</span><span class="star off">★★</span></div></div>
  <div class="abs card" style="left:744px"><div class="img blonde" role="img" aria-label="Product photo: blonde braided wig"></div><div class="n">Lorem Ipsum Name</div><div class="p"><s>$ 12.00</s><em>$ 09.00</em></div><div class="stars"><span class="star">★★★</span><span class="star off">★★</span></div></div>
  <div class="abs card" style="left:850px"><div class="img greendress" role="img" aria-label="Product photo: green dirndl with beer stein"></div><div class="n">Lorem Ipsum Name</div><div class="p"><s>$ 12.00</s><em>$ 09.00</em></div><div class="stars"><span class="star">★★★</span><span class="star off">★★</span></div></div>

  <div class="abs partners">
    <div class="partner" style="left:48px"><i></i>Feestpost</div>
    <div class="sep" style="left:145px"></div>
    <div class="partner" style="left:182px">Parcelo</div>
    <div class="sep" style="left:292px"></div>
    <div class="partner" style="left:320px">PayDirect</div>
    <div class="sep" style="left:389px"></div>
    <div class="partner" style="left:428px">Paywell</div>
  </div>

  <div class="abs foot site">
    <h4>Site Info</h4><div class="rule"></div>
    <ul style="position:absolute;left:0;top:32px"><li>Shipping and Return</li><li>Right of Withdraw</li><li>Imprint</li><li>Privacy Notice</li><li>Contact Us</li></ul>
    <ul style="position:absolute;left:141px;top:32px"><li>Create New Account</li><li>Login</li><li>Track your order</li><li>Shopping Cart</li></ul>
  </div>
  <div class="abs foot blog">
    <h4>Latest Blog Post</h4><div class="rule" style="width:95px"></div>
    <ul style="margin-top:8px"><li>Lorem Ipsum is simply dummy text</li><li>Lorem Ipsum is simply dummy text</li><li style="border:0">Lorem Ipsum is simply dummy text</li></ul>
  </div>
  <div class="abs foot letter">
    <h4>Newsletter</h4><div class="rule"></div>
    <div class="mail"><span>email@example.com</span><b>GO</b></div>
  </div>
  <div class="abs foot social">
    <h4>Social Link</h4><div class="rule"></div>
    <div class="dots"><i></i><i></i><i></i><i></i></div>
  </div>

  <div class="abs copyline"></div>
  <div class="abs copy">Copyright © 2014 Company Name</div>
  <div class="abs cards"><span>Paywell</span><span>Cardo</span><span>Vexa</span></div>

</div>
</body>
</html>
```